I want a business card that is going to show a creative spark but without limiting me to an industry. Something edgy but that wont go out of date. I want it state My business name Serafina Loire, profession - Professional Makeup Artist contact number and email

My service is to provide makeup services from bridal, fashion, photography, film, TV and so on. It is creative and different so i want that to be reflected.

I would like the card double sided.
Updates

 I would LOVE a background on my card something like this image... i can supply an image to be formed like this

Please use the image uploaded

Can we try using the image provided on one side of the card and then writing and details on the other side

Target Market(s)

I am targeting a wide range of people from Creative directors to the individual eg. bride

Industry/Entity Type

Business

Requirements
Must have
• Name: Delphine Hartwell
contact numbe 0417853120
email address:info@serafinaloire.com
website: www.serafinaloire.com
One of the images attached

professional makeup artist / hair stylist

I want it to show creativity
Nice to have
• logo, Double-sided card
Should not have
• the design should not use tradional style. Or images that are not my own

```html
<!DOCTYPE html>
<html lang="en">
<head>
<meta charset="utf-8">
<title>Serafina Loire – Business Card</title>
<link rel="stylesheet" href="https://fonts.googleapis.com/css2?family=Open+Sans:wght@300&family=Special+Elite&display=swap">
<style>
  :root {
    --page: #ffffff;
    --paper: #fdf8d6;
    --paper-line: rgba(214, 196, 140, 0.10);
    --crimson: #d8185c;
    --ribbon: #d61a5a;
    --ink-light: #ffffff;
    --photo-violet: #3b1f8a;
    --photo-plum: #7a2a6e;
    --photo-amber: #e2914f;
    --photo-cream: #f6d9a8;
  }

  * { box-sizing: border-box; margin: 0; padding: 0; }

  html, body {
    width: 1200px;
    height: 1200px;
    overflow: hidden;
    background: var(--page);
  }

  .canvas {
    position: relative;
    width: 1200px;
    height: 1200px;
  }

  .card {
    position: absolute;
    left: 73px;
    width: 1051px;
    height: 529px;
    overflow: hidden;
    background-color: var(--paper);
    background-image: repeating-linear-gradient(90deg, transparent 0 5px, var(--paper-line) 5px 7px);
  }

  .card--front { top: 40px; }
  .card--back  { top: 611px; }

  .portrait {
    position: absolute;
    top: 0;
    height: 529px;
    background: linear-gradient(115deg, var(--photo-violet) 0%, var(--photo-plum) 35%, var(--photo-amber) 62%, var(--photo-cream) 80%, var(--photo-plum) 100%);
  }

  .portrait--left {
    left: 0;
    width: 285px;
    clip-path: polygon(0 0, 200px 0, 214px 40px, 228px 110px, 236px 200px, 250px 300px, 262px 400px, 285px 529px, 0 529px);
  }

  .portrait--right {
    right: 0;
    width: 280px;
    background: linear-gradient(245deg, var(--photo-violet) 0%, var(--photo-plum) 35%, var(--photo-amber) 62%, var(--photo-cream) 80%, var(--photo-plum) 100%);
    clip-path: polygon(80px 0, 280px 0, 280px 529px, 0 529px, 22px 400px, 34px 300px, 48px 200px, 58px 110px, 68px 40px);
  }

  .typewriter {
    font-family: "Special Elite", "Courier New", monospace;
    line-height: 1;
  }

  .profession {
    position: absolute;
    top: 18px;
    left: 0;
    width: 100%;
    text-align: center;
    font-size: 32px;
    color: var(--crimson);
    letter-spacing: 0.5px;
  }

  .name {
    position: absolute;
    left: 0;
    width: 100%;
    text-align: center;
    font-family: "Open Sans", "Segoe UI", sans-serif;
    font-weight: 300;
    color: var(--crimson);
  }

  .card--front .name {
    top: 62px;
    font-size: 128px;
    line-height: 108px;
    letter-spacing: -1px;
  }

  .card--back .name {
    top: 96px;
    left: -16px;
    font-size: 142px;
    line-height: 124px;
    letter-spacing: -1px;
  }

  .contact-label {
    position: absolute;
    left: 0;
    width: 100%;
    text-align: center;
    font-size: 29px;
    color: var(--crimson);
  }

  .contact-label--phone { top: 307px; }
  .contact-label--email { top: 410px; }

  .ribbon {
    position: absolute;
    left: 307px;
    width: 456px;
    height: 64px;
  }

  .ribbon svg {
    position: absolute;
    inset: 0;
  }

  .ribbon--phone { top: 343px; }
  .ribbon--email { top: 444px; }

  .ribbon__text {
    position: absolute;
    inset: 0;
    display: flex;
    align-items: center;
    justify-content: center;
    color: var(--ink-light);
  }

  .ribbon--phone .ribbon__text { font-size: 27px; }
  .ribbon--email .ribbon__text { font-size: 23px; }

  .back-detail {
    position: absolute;
    left: 0;
    width: 100%;
    text-align: center;
    color: var(--crimson);
  }

  .back-detail--title { top: 392px; font-size: 28px; }
  .back-detail--web   { top: 438px; font-size: 26px; }
</style>
</head>
<body>
<main class="canvas">

  <section class="card card--front" aria-label="Card front">
    <div class="portrait portrait--left" role="img" aria-label="Tinted portrait photograph of the makeup artist, facing right"></div>
    <div class="portrait portrait--right" role="img" aria-label="Mirrored tinted portrait photograph of the makeup artist, facing left"></div>

    <p class="profession typewriter">Professional Makeup Artist</p>
    <h1 class="name">Serafina<br>Loire</h1>

    <p class="contact-label contact-label--phone typewriter">contact number</p>
    <div class="ribbon ribbon--phone">
      <svg viewBox="0 0 456 64" width="456" height="64" aria-hidden="true">
        <polygon fill="var(--ribbon)" points="0,2 456,0 438,21 452,32 440,44 454,62 4,64 22,44 8,32 20,21"/>
      </svg>
      <span class="ribbon__text typewriter">0417853120</span>
    </div>

    <p class="contact-label contact-label--email typewriter">email address</p>
    <div class="ribbon ribbon--email">
      <svg viewBox="0 0 456 64" width="456" height="64" aria-hidden="true">
        <polygon fill="var(--ribbon)" points="2,0 454,2 436,21 450,32 438,44 456,64 0,62 20,44 6,32 18,21"/>
      </svg>
      <span class="ribbon__text typewriter">info@serafinaloire.com</span>
    </div>
  </section>

  <section class="card card--back" aria-label="Card back">
    <h2 class="name">Serafina<br>Loire</h2>
    <p class="back-detail back-detail--title typewriter">Makeup Artist / Hair Stylist</p>
    <p class="back-detail back-detail--web typewriter">www.serafinaloire.com</p>
  </section>

</main>
</body>
</html>
```